Virtual Assistant/Online Marketing Business Card/Stationary

I need a professional but modern business card/stationary for my company in Dallas called Brivolo. Brivolo is a virtual assistant specializing in online marketing. I would like a unique design that stands out and makes my brand clear. Incorporating the logo is a must and have attached it to this brief.

Target Market(s)

small business owners & entrepreneurs, 35-65

Industry/Entity Type

Business

Contact Information for Business Card

Maren Tolk
marentolk@brivolo.biz
(555) 271-9064
brivolo.biz

Font styles to use
Sans Serif

Colors
f04a50
3176b5
9bcb3c

Requirements
Must have
• Colors that match the logo colors. Logo integration

```html
<!DOCTYPE html>
<html lang="en">
<head>
<meta charset="utf-8">
<title>Brivolo — Business Card</title>
<link rel="stylesheet" href="https://fonts.googleapis.com/css2?family=Roboto:wght@400;700&display=swap">
<style>
  :root {
    --backdrop: #dcdcdc;
    --card: #ffffff;
    --ink: #2b2b2b;
    --green: #7cc24a;
    --red: #c9412f;
    --teal: #3b9fa6;
    --blue: #2a6f9b;
    --on-band: #ffffff;
  }
  * { margin: 0; padding: 0; box-sizing: border-box; }
  html, body { width: 1200px; height: 750px; overflow: hidden; }
  body {
    background: var(--backdrop);
    font-family: "Roboto", Arial, sans-serif;
    display: flex;
    align-items: center;
    justify-content: center;
    gap: 60px;
  }
  .card {
    width: 480px;
    height: 280px;
    background: var(--card);
    border-radius: 14px;
    overflow: hidden;
    box-shadow: 0 6px 18px rgba(0,0,0,0.12);
    position: relative;
  }
  .card-front { display: flex; }
  .brand-panel {
    width: 46%;
    display: flex;
    align-items: center;
    justify-content: center;
  }
  .wordmark {
    font-weight: 700;
    font-size: 34px;
    color: var(--ink);
    letter-spacing: 0.5px;
    display: flex;
    align-items: center;
    gap: 10px;
  }
  .wordmark-dot {
    width: 14px;
    height: 14px;
    background: var(--red);
    display: inline-block;
  }
  .contact-bands {
    width: 54%;
    display: flex;
    flex-direction: column;
    list-style: none;
  }
  .band {
    flex: 1;
    display: flex;
    align-items: center;
    gap: 12px;
    padding-left: 30px;
    color: var(--on-band);
    font-size: 13px;
  }
  .band-name { background: var(--green); font-size: 14px; text-transform: uppercase; letter-spacing: 0.5px; }
  .band-email { background: var(--red); }
  .band-phone { background: var(--teal); }
  .band-web { background: var(--blue); }
  .band svg { width: 16px; height: 16px; flex: none; }
  .card-back {
    display: flex;
    align-items: center;
    justify-content: center;
  }
  .edge-strip {
    position: absolute;
    left: 0; top: 0; bottom: 0;
    width: 10px;
    display: flex;
    flex-direction: column;
  }
  .edge-strip span { flex: 1; }
  .edge-strip .g { background: var(--green); }
  .edge-strip .r { background: var(--red); }
  .edge-strip .t { background: var(--teal); }
  .edge-strip .b { background: var(--blue); }
</style>
</head>
<body>
  <section class="card card-front">
    <div class="brand-panel">
      <div class="wordmark"><span class="wordmark-dot"></span>Brivolo</div>
    </div>
    <ul class="contact-bands">
      <li class="band band-name">
        <svg viewBox="0 0 16 16"><rect x="1" y="1" width="14" height="14" rx="2" fill="#fff"/><circle cx="8" cy="6.5" r="2.5" fill="#7cc24a"/><path d="M3.5 13c.8-2.5 2.5-3.5 4.5-3.5s3.7 1 4.5 3.5z" fill="#7cc24a"/></svg>
        Maren Tolk
      </li>
      <li class="band band-email">
        <svg viewBox="0 0 16 16"><rect x="1" y="3" width="14" height="10" rx="1.5" fill="#fff"/><path d="M2 4.5l6 4.5 6-4.5" fill="none" stroke="#c9412f" stroke-width="1.4"/></svg>
        marentolk@brivolo.biz
      </li>
      <li class="band band-phone">
        <svg viewBox="0 0 16 16"><rect x="4" y="1" width="8" height="14" rx="1.5" fill="#fff"/><rect x="5.5" y="3" width="5" height="8" fill="#3b9fa6"/><circle cx="8" cy="13" r="0.9" fill="#3b9fa6"/></svg>
        (555) 271-9064
      </li>
      <li class="band band-web">
        <svg viewBox="0 0 16 16"><rect x="1" y="2" width="14" height="12" rx="1.5" fill="#fff"/><rect x="1" y="2" width="14" height="3" fill="#d6e6f2"/><path d="M3.5 8h9M3.5 10.5h6" stroke="#2a6f9b" stroke-width="1.2"/></svg>
        brivolo.biz
      </li>
    </ul>
  </section>

  <section class="card card-back">
    <div class="edge-strip" aria-hidden="true">
      <span class="g"></span><span class="r"></span><span class="t"></span><span class="b"></span>
    </div>
    <div class="wordmark"><span class="wordmark-dot"></span>Brivolo</div>
  </section>
</body>
</html>
```